Copper Vesper - the new thriller in the Tidemarks series by award-winning author Marta K. Overby

Looking for an book cover design for the 4th book in the Tidemarks series by Marta K. Overby. Covers from the first 3 books are attached. Would like to keep a series look going, so possibly using a hand holding a paint brush might work - but not tied down to showing a hand on the cover. Most of the book takes place in a rustic Arizona desert estate in a national forest - so something depicting a desert scene might work too. The cover needs to convey a "thriller" feeling. Attached is our design template with needed specs. Also attached are two other covers for inspiration:

SALT UNDER THE ORCHARD - something like this could work in the key were a paintbrush and the scene is set in the Arizona desert

ONE SPARROW AT NOON - this could work too with Arizona desert setting

Here's the synopsis of COPPER VESPER:

Her life ended and she is disappointed to discover she is still alive.

With all ties to her handler or anyone connected to her life as a hired killer, she struggles to understand who and even what she has become. She knows she doesn’t want to kill again. And yes, danger finds her and she responds, animal-like, in the only way she knows how.

In this mood of absolute bereavement, she comes across Petra Vasquell, a world famous artist who has spent the last three decades living a hermit-like existence on a rustic desert estate in a national forest.

Petra invites her to stay on to assist the old woman who will, in return, mentor our narrator as she deepens her own interest in art.

What is not at first apparent is that elements of Petra’s past are shrouded in danger, sorrow and darkness and rather than growing as an artist, she soon finds herself enmeshed in a dangerous mystery with strands that stretch decades into the past.

```html
<!DOCTYPE html>
<html lang="en">
<head>
<meta charset="utf-8">
<title>Copper Vesper — Book Cover</title>
<link href="https://fonts.googleapis.com/css2?family=Oswald:wght@400;500;600&family=Raleway:wght@300&display=swap" rel="stylesheet">
<style>
  :root {
    --page-bg: #ffffff;
    --sky-top: #1c1d1f;
    --sky-mid: #3a3b3d;
    --horizon-glow: #8a6a44;
    --desert-dark: #1a1511;
    --desert-warm: #3d2c1c;
    --paint-red: #e8202a;
    --paint-red-deep: #b8141b;
    --text-light: #ffffff;
    --hand-tone: #c9a58a;
  }
  * { margin: 0; padding: 0; box-sizing: border-box; }
  html, body {
    width: 1200px;
    height: 1000px;
    overflow: hidden;
    background: var(--page-bg);
  }
  .canvas {
    position: relative;
    width: 1200px;
    height: 1000px;
    background: var(--page-bg);
  }
  .book-cover {
    position: absolute;
    left: 38px;
    top: 30px;
    width: 635px;
    height: 940px;
    overflow: hidden;
  }
  .cover-scene {
    position: absolute;
    inset: 0;
    background: linear-gradient(180deg,
      var(--sky-top) 0%,
      var(--sky-mid) 22%,
      #4a4845 34%,
      var(--horizon-glow) 38%,
      #2a2420 41%,
      var(--desert-warm) 58%,
      #2b2017 78%,
      var(--desert-dark) 100%);
  }
  .hand-with-brush {
    position: absolute;
    left: 40px;
    top: 430px;
    width: 390px;
    height: 510px;
    background: radial-gradient(ellipse at 60% 45%, rgba(201,165,138,0.55) 0%, rgba(201,165,138,0.18) 45%, rgba(201,165,138,0) 72%);
  }
  .paint-stroke {
    position: absolute;
    left: 280px;
    top: 0;
    width: 32px;
    height: 440px;
    background: var(--paint-red);
  }
  .endorsement {
    position: absolute;
    top: 68px;
    left: 0;
    width: 100%;
    text-align: center;
    color: var(--text-light);
    font-family: 'Oswald', sans-serif;
  }
  .endorsement-quote {
    font-size: 38px;
    font-weight: 500;
    line-height: 1.05;
    letter-spacing: -0.5px;
  }
  .endorsement-quote .small-word { font-size: 24px; }
  .endorsement-source {
    font-size: 17px;
    font-weight: 500;
    line-height: 1.2;
    margin-left: 40px;
  }
  .endorsement-source .small-word { font-size: 12px; }
  .cover-title {
    position: absolute;
    left: 0;
    top: 190px;
    width: 635px;
    height: 270px;
  }
  .cover-title text {
    font-family: 'Oswald', sans-serif;
    font-weight: 500;
    font-size: 132px;
    letter-spacing: -2px;
  }
  .title-light { fill: var(--text-light); }
  .title-painted { fill: var(--paint-red-deep); }
  .format-label {
    position: absolute;
    left: 373px;
    top: 742px;
    color: var(--text-light);
    font-family: 'Raleway', sans-serif;
    font-weight: 300;
    font-size: 29px;
    letter-spacing: 1px;
  }
  .author-name {
    position: absolute;
    left: 0;
    top: 788px;
    width: 100%;
    text-align: center;
    color: var(--text-light);
    font-family: 'Oswald', sans-serif;
    font-weight: 500;
    font-size: 58px;
    letter-spacing: -0.5px;
  }
</style>
</head>
<body>
<main class="canvas">
  <section class="book-cover">
    <div class="cover-scene" role="img" aria-label="Arizona desert at dusk with saguaro cacti, distant dark mountains and a cloudy night sky"></div>
    <div class="paint-stroke"></div>
    <div class="hand-with-brush" role="img" aria-label="A hand holding a paintbrush loaded with red paint, painting a vertical stroke upward"></div>

    <div class="endorsement">
      <p class="endorsement-quote">“PROVOCATIVE <span class="small-word">AND</span> POWERFUL.”</p>
      <p class="endorsement-source">-RENATA HOLLOWAY, <span class="small-word">HARBOR LEDGER BEST SELLING</span> - AUTHOR</p>
    </div>

    <svg class="cover-title" viewBox="0 0 635 270" aria-label="Copper Vesper">
      <defs>
        <clipPath id="stroke-clip">
          <rect x="280" y="0" width="32" height="270"/>
        </clipPath>
      </defs>
      <g class="title-light" text-anchor="middle">
        <text x="317.5" y="126">COPPER</text>
        <text x="317.5" y="256">VESPER</text>
      </g>
      <g class="title-painted" text-anchor="middle" clip-path="url(#stroke-clip)" aria-hidden="true">
        <text x="317.5" y="126">COPPER</text>
        <text x="317.5" y="256">VESPER</text>
      </g>
    </svg>

    <p class="format-label">A NOVEL</p>
    <p class="author-name">MARTA K. OVERBY</p>
  </section>
</main>
</body>
</html>
```